RW Business Card Design

My company provides advising/training and coaching services to business owners who want better financial results and better work/life balance. We help them through creating custom plans supported with education, strategic thinking and accountability.

We also help through some online courses which are geared to smaller businesses.
Updates

please also include our nth american contact # +1 555 208 4471

Industry/Entity Type

Financial

Contact Information for Business Card

Morgan Halberd
morgan@morganhalberd-example.com
+61 400 555 917
www.morganhalberd-example.com

```html
<!DOCTYPE html>
<html lang="en">
<head>
<meta charset="utf-8">
<title>RW Business Card Design</title>
<link rel="stylesheet" href="https://fonts.googleapis.com/css2?family=Open+Sans:wght@300;400&display=swap">
<style>
  :root {
    --backdrop: #e6e6e4;
    --card: #ffffff;
    --card-edge: #d9dadc;
    --brand-blue: #2b87d1;
    --brand-grey: #8e9094;
    --ink: #1f2226;
    --ghost: #eceef2;
  }
  * { margin: 0; padding: 0; box-sizing: border-box; }
  html, body { width: 1200px; height: 900px; overflow: hidden; }
  body {
    background: var(--backdrop);
    font-family: "Open Sans", Arial, sans-serif;
    display: flex;
    align-items: center;
    justify-content: center;
    gap: 60px;
  }
  .card {
    position: relative;
    width: 520px;
    height: 297px;
    background: var(--card);
    border: 1px solid var(--card-edge);
    box-shadow: 0 10px 24px rgba(0,0,0,0.12);
    overflow: hidden;
  }
  .ghost-mark {
    position: absolute;
    border-radius: 50%;
    background: var(--ghost);
  }
  .brand {
    position: absolute;
    display: flex;
    align-items: center;
    gap: 12px;
  }
  .brand-dot {
    border-radius: 50%;
    background: var(--brand-blue);
    flex: none;
  }
  .brand-name {
    font-weight: 300;
    color: var(--brand-grey);
    text-transform: uppercase;
    letter-spacing: 0.5px;
    white-space: nowrap;
  }

  /* contact side */
  .card--contact .ghost-mark { width: 200px; height: 200px; right: 30px; top: 48px; }
  .card--contact .brand { left: 34px; top: 40px; }
  .card--contact .brand-dot { width: 34px; height: 34px; }
  .card--contact .brand-name { font-size: 21px; }
  .contact-list {
    position: absolute;
    left: 34px;
    bottom: 34px;
    list-style: none;
    font-size: 14px;
    color: var(--ink);
    line-height: 25px;
  }
  .contact-list li { display: flex; align-items: center; gap: 9px; }
  .contact-list svg { width: 12px; height: 12px; flex: none; }

  /* front side */
  .card--front .ghost-mark { width: 210px; height: 210px; right: -20px; top: 20px; }
  .card--front .brand { left: 40px; top: 50%; transform: translateY(-50%); gap: 22px; }
  .card--front .brand-dot { width: 120px; height: 120px; }
  .card--front .brand-name { font-size: 26px; }
</style>
</head>
<body>
  <section class="card card--contact">
    <div class="ghost-mark" role="img" aria-label="Faint brand mark decoration"></div>
    <div class="brand">
      <span class="brand-dot"></span>
      <span class="brand-name">Morgan Halberd</span>
    </div>
    <ul class="contact-list">
      <li>
        <svg viewBox="0 0 12 12" aria-hidden="true"><path d="M3 1 L5 3.5 L4 5 Q5.5 7 7 8 L8.5 7 L11 9 L9.5 11 Q4 10 1 2.5 Z" fill="var(--brand-blue)"/></svg>
        +61 400 555 917
      </li>
      <li>
        <svg viewBox="0 0 12 12" aria-hidden="true"><path d="M3 1 L5 3.5 L4 5 Q5.5 7 7 8 L8.5 7 L11 9 L9.5 11 Q4 10 1 2.5 Z" fill="var(--brand-blue)"/></svg>
        +1 555 208 4471
      </li>
      <li>
        <svg viewBox="0 0 12 12" aria-hidden="true"><rect x="0.5" y="2" width="11" height="8" fill="var(--brand-blue)"/><path d="M0.5 2 L6 7 L11.5 2" fill="none" stroke="#fff" stroke-width="1"/></svg>
        morgan@morganhalberd-example.com
      </li>
      <li>
        <svg viewBox="0 0 12 12" aria-hidden="true"><circle cx="6" cy="6" r="5.5" fill="var(--brand-blue)"/><path d="M0.5 6 H11.5 M6 0.5 V11.5 M2 3 Q6 5 10 3 M2 9 Q6 7 10 9" fill="none" stroke="#fff" stroke-width="0.8"/></svg>
        www.morganhalberd-example.com
      </li>
    </ul>
  </section>

  <section class="card card--front">
    <div class="ghost-mark" role="img" aria-label="Faint brand mark decoration"></div>
    <div class="brand">
      <span class="brand-dot"></span>
      <span class="brand-name">Morgan Halberd</span>
    </div>
  </section>
</body>
</html>
```